Plakate für einen Immobilienmakler
Zielgruppe
Briefing für Plakatgestaltung – Immobilienvermietung
Ziel des Plakats:
Ich bin Immobilienmakler und benötige ein aussagekräftiges, aufmerksamkeitsstarkes Plakat zur Vermietung einer Immobilie. Das Plakat wird direkt in der zu vermietenden Immobilie angebracht und soll auf einen Blick klar machen, dass die Fläche zur Miete steht – idealerweise mit der Aussage: “Zu vermieten” oder “Fläche zu mieten” in den Fokus gesetzt.
Format und Einsatzort:
Das Objekt verfügt über drei sehr große Schaufenster (je ca. 3 x 4 Meter). Die Plakate werden in diese Fenster gehängt und sollen sowohl von der Straße aus gut lesbar sein als auch optisch professionell und hochwertig wirken. Wichtig ist, dass die Gestaltung auch aus einiger Entfernung (z. B. von gegenüberliegenden Straßenseiten) klar verständlich bleibt.
Stil und Designvorgaben:
Ich habe in der Vergangenheit bereits Werbematerialien für meine Marke verwendet (diese Plakate, Grafiken und Anzeigen füge ich dem Auftrag bei). Diese sollen als stilistische Orientierung dienen. Gerne darf das Design leicht weiterentwickelt werden, aber der Wiedererkennungswert meiner Marke soll erhalten bleiben.
Folgende Elemente sollen integriert werden:
• Mein Logo (wird als Datei bereitgestellt)
• Ein Porträtbild von mir (wird mitgeliefert)
• Klar erkennbare Kontaktinformationen (Telefon, Website, ggf. QR-Code)
• Auf Wunsch auch ein Call-to-Action, wie z. B. „Jetzt Besichtigung anfragen!“ oder „Kontaktieren Sie mich direkt!“
Optional – je nach Platz:
• Ein Bild der Immobilie oder ein Hinweis auf die Art der Fläche (z. B. “Gewerbefläche”, “Ladenfläche”, “Bürofläche”)
• Kurztext mit Details wie Größe, Lage oder Bezugstermin
Wichtig:
Das Hauptziel ist es, die Passanten direkt zu informieren: Diese Immobilie steht zur Miete – und ich bin der Ansprechpartner. Bitte darauf achten, dass die W..
Aufgabenstellung
Mein Logo soll dirn sein es soll klar sein und die Kunden sollen leicht meine Adresse scannen können oder abschreiben

```html
<!DOCTYPE html>
<html lang="de">
<head>
<meta charset="utf-8">
<title>Zu Vermieten – Plakat</title>
<link rel="stylesheet" href="https://fonts.googleapis.com/css2?family=DM+Serif+Display&family=Inter:wght@400;600;700&display=swap">
<style>
  :root {
    --scene-warm: #b8864f;
    --scene-deep: #7a5434;
    --scene-light: #e9ddcc;
    --scene-floor: #c98a4e;
    --portrait-top: #34508f;
    --portrait-bottom: #1b2f63;
    --headline: #ffffff;
    --band-bg: #ffffff;
    --ink: #111111;
    --rule: #2a2a2a;
  }
  * { margin: 0; padding: 0; box-sizing: border-box; }
  html, body { width: 1200px; height: 900px; overflow: hidden; background: var(--band-bg); }
  .poster { position: relative; width: 1200px; height: 900px; font-family: "Inter", sans-serif; color: var(--ink); }

  .interior-scene {
    position: absolute; left: 0; top: 0; width: 1200px; height: 719px;
    background:
      radial-gradient(ellipse 30% 40% at 52% 40%, var(--scene-warm) 0%, transparent 70%),
      linear-gradient(180deg, var(--scene-light) 0%, #d3ba9b 35%, var(--scene-deep) 62%, var(--scene-floor) 80%, #a8723f 100%);
  }

  .agent-portrait {
    position: absolute; left: 213px; top: 104px; width: 402px; height: 615px;
    border-radius: 150px 150px 0 0;
    background: linear-gradient(180deg, var(--portrait-top) 0%, var(--portrait-bottom) 100%);
  }

  .headline {
    position: absolute; left: 600px; top: 185px; width: 560px;
    font-family: "DM Serif Display", serif; font-weight: 400;
    font-size: 118px; line-height: 1.02; color: var(--headline);
    text-align: center; text-shadow: 0 2px 8px rgba(0,0,0,0.18);
  }

  .contact-band {
    position: absolute; left: 0; top: 719px; width: 1200px; height: 181px;
    background: var(--band-bg);
  }
  .agent-contact { position: absolute; left: 62px; top: 39px; }
  .agent-name { font-size: 17px; font-weight: 600; margin-bottom: 6px; }
  .agent-phone { font-size: 22px; font-weight: 700; line-height: 1.32; }

  .divider { position: absolute; top: 40px; width: 1.5px; height: 80px; background: var(--rule); }
  .divider--first { left: 243px; }
  .divider--second { left: 516px; }

  .property-info { position: absolute; left: 264px; top: 38px; font-size: 17px; line-height: 1.76; }

  .call-to-action { position: absolute; left: 536px; top: 62px; font-size: 21px; font-weight: 700; line-height: 1.45; }

  .brand-name {
    position: absolute; right: 57px; top: 76px;
    font-size: 29px; font-weight: 700; letter-spacing: 0.5px; color: var(--ink);
  }
</style>
</head>
<body>
  <main class="poster">
    <div class="interior-scene" role="img" aria-label="Heller, leerer Innenraum der Mietfläche mit Holzboden, Pendelleuchte und Zimmerpflanzen"></div>
    <div class="agent-portrait" role="img" aria-label="Porträt des Immobilienmaklers im dunkelblauen Sakko mit verschränkten Armen"></div>

    <h1 class="headline">Zu<br>Vermieten</h1>

    <footer class="contact-band">
      <div class="agent-contact">
        <p class="agent-name">Kessler</p>
        <p class="agent-phone">401 17<br>386 512</p>
      </div>
      <span class="divider divider--first"></span>
      <div class="property-info">
        <p>Ladenfläche</p>
        <p>Lindenstraße 12</p>
        <p>Zentrum Nord</p>
      </div>
      <span class="divider divider--second"></span>
      <p class="call-to-action">Jetzt Besichtigung<br>anfragen!</p>
      <p class="brand-name">HAUSWERK</p>
    </footer>
  </main>
</body>
</html>
```